lotus bowl vietnamese restaurant in need of a new menu

a family owned vietnamese restaurant in need of a new menu design that is fun, classy, and yet simple. menu that will catch the customers eyes. easy to read yet flows nicely. like to use the color green (basil green color) creme yellow and maroon. open to other colors as long as it looks nice together. our restaurant is family oriented, casual yet has a nice ambiance atmosphere.
prefer 11x17 portrait double sided. attached is our menu with the current price updated so use the info on this to start creating! looking for something unique, professional and one of a kind menu!
please use your own creative layout and design. we are open to ideas. the files uploaded are the updated prices and the logo is to use whichever one you feel goes with the menu.
Reason: don't see anything we like so far...please be creative!
Target Market(s)
restaurant consumers
Industry/Entity Type
Restaurant
Look and feel

```html
<!DOCTYPE html>
<html lang="en">
<head>
<meta charset="utf-8">
<title>Lotus Bowl – Take Out Menu</title>
<link href="https://fonts.googleapis.com/css2?family=Roboto+Condensed:wght@400;700&family=Roboto:wght@700;900&family=Oswald:wght@300&display=swap" rel="stylesheet">
<style>
:root{
  --page:#d4f36c;
  --paper:#fbfbf1;
  --frame:#a8ec6a;
  --basil:#3ee01a;
  --maroon:#c4161c;
  --ink:#161616;
  --pill:#8ee866;
  --flame:#f47b20;
}
*{margin:0;padding:0;box-sizing:border-box}
html,body{width:1200px;height:1200px;overflow:hidden;background:var(--page)}
.menu{
  position:absolute;left:222px;top:14px;width:756px;height:1172px;
  background:var(--paper);border:5px solid var(--frame);
  box-shadow:4px 6px 8px rgba(0,0,0,.35);overflow:hidden;
  font-family:"Roboto Condensed",Arial Narrow,sans-serif;color:var(--ink);
}
.bowl-photo{
  position:absolute;left:-8px;top:-110px;width:250px;height:318px;border-radius:50%;
  border:5px solid var(--maroon);
  background:radial-gradient(circle at 45% 60%,#e8ead0 0%,#8ccf4a 35%,#3f8e22 75%,#2f6d1a 100%);
}
.brand{position:absolute;left:40px;top:220px;width:300px;text-align:center}
.brand-name{font-family:Roboto,sans-serif;font-weight:700;font-size:37px;color:var(--ink);display:flex;align-items:center;justify-content:center;gap:10px}
.brand-mark{width:14px;height:14px;background:var(--basil)}
.brand-sub{font-family:Roboto,sans-serif;font-weight:700;font-size:25px;color:var(--basil);margin-top:6px}
.takeout{
  position:absolute;left:55px;top:314px;width:270px;height:44px;background:var(--maroon);
  color:#fff;font-family:Oswald,sans-serif;font-weight:300;font-size:34px;letter-spacing:2px;
  text-align:center;line-height:44px;
}
.divider{position:absolute;left:376px;top:22px;width:2px;height:1120px;background:var(--maroon)}
.divider::before,.divider::after{content:"";position:absolute;left:-3px;width:8px;height:8px;background:var(--maroon);transform:rotate(45deg)}
.divider::before{top:10px}.divider::after{bottom:10px}
.item,.section{position:absolute;left:18px;width:340px}
.col-r{left:394px;width:345px}
.section{color:var(--maroon);font-weight:700;font-size:15px;line-height:1.05}
.item h3{font-size:12px;font-weight:700;line-height:1.2}
.item p{font-size:10px;line-height:1.25;text-transform:uppercase}
.item p b{font-weight:700}
.item p small{text-transform:none;font-size:9px}
.narrow{width:260px}
.flame{display:inline-block;width:8px;height:11px;background:var(--flame);border-radius:50% 50% 50% 50%/70% 70% 30% 30%;margin-left:5px;vertical-align:-1px}
.photo{position:absolute;border:3px solid var(--basil);border-radius:6px}
.p-rolls{background:linear-gradient(135deg,#7fc46a,#e8b3a6,#5aa04a)}
.p-egg{background:linear-gradient(135deg,#e9a84a,#c46f24,#f0c98a)}
.p-wonton{background:linear-gradient(135deg,#f3e7d6,#e7b07a,#c85a2a)}
.p-shrimp{background:linear-gradient(135deg,#f28b50,#fbe0c2,#2f6ea8)}
.p-salad{background:linear-gradient(135deg,#6aa54a,#d9d3b0,#a67a4a)}
.p-soup{background:linear-gradient(135deg,#e8e2c9,#b6d08a,#d97a5a)}
.p-goi{background:linear-gradient(135deg,#4a8a5a,#e3c9c0,#8fbf9a)}
.p-beef{background:linear-gradient(135deg,#e07a3a,#5a2a1a,#e8d9b0)}
.p-bun{background:linear-gradient(135deg,#6ab14a,#f08a50,#f3ede0)}
.extras{
  position:absolute;left:394px;top:807px;width:343px;height:52px;background:var(--pill);border-radius:4px;
  display:flex;gap:10px;padding:5px 8px 0 26px;font-size:6.6px;line-height:1.3;text-transform:uppercase;
}
.extras ul{list-style:none;flex:1}
.extras li::before{content:"* "}
.extras em{text-transform:none}
.contact{
  position:absolute;left:394px;top:1131px;width:343px;height:19px;background:var(--pill);border-radius:10px;
  font-size:9px;font-weight:700;text-align:center;line-height:19px;word-spacing:1px;
}
</style>
</head>
<body>
<main class="menu">
  <div class="bowl-photo" role="img" aria-label="Photo of a bowl of pho topped with herbs, sprouts and lime"></div>
  <div class="brand">
    <div class="brand-name"><span>Lotus Bowl</span><span class="brand-mark"></span></div>
    <div class="brand-sub">Vietnamese Restaurant</div>
  </div>
  <div class="takeout">TAKE OUT MENU</div>

  <div class="divider"></div>

  <!-- Left column -->
  <h2 class="section" style="top:390px">APPETIZERS</h2>
  <div class="item" style="top:409px;width:360px"><p style="font-size:8.5px"><b>SPRING ROLLS (2)</b> COMES WITH LETTUCE, VERMICELLI NOODLES ROLLED<br>IN RICE PAPER SERVED WITH PEANUT SAUCE WITH CHOICE OF: <small>(cannot be mixed):</small></p></div>
  <div class="item" style="top:438px"><h3>1. GOI CUON TOM &amp; THIT HEO | 4.50</h3><p>SHRIMP &amp; PORK SPRING ROLLS</p></div>
  <div class="item" style="top:476px"><h3>2. GOI CUON THIT HEO / GA / OR BO NUONG | 5.50</h3><p>CHOICE OF: GRILLED PORK / GRILLED CHICKEN OR<br>GRILLED BEEF SPRING ROLLS</p></div>
  <div class="item" style="top:526px"><h3>3. BI CUON | 4.50</h3><p>PORK SKIN ROASTED WITH RICE POWDER SPRING ROLLS</p></div>
  <div class="item" style="top:564px"><h3>4. CHA GIO (2) | 4.50</h3><p>FRIED EGGROLLS WITH SHRIMP, PORK &amp;<br>VEGETABLES ROLLED IN EGG WRAP</p></div>
  <div class="item" style="top:614px"><h3>5. CANH GA NUOC MAM (6) | 7.95</h3><p>FRIED CHICKEN WINGS</p></div>
  <div class="item" style="top:653px"><h3>6. GIO TOM (4)| 5.95</h3><p>FRIED SHRIMP ROLLS</p></div>
  <div class="item" style="top:691px"><h3>7. CA VIEN CHIEN (8) | 4.95</h3><p style="font-size:11px">FRIED FISH BALLS</p></div>
  <div class="item" style="top:733px"><h3>8. CHAO TOM (2) | 7.95</h3><p>GRILLED SHRIMP PASTE WRAPPED<br>AROUND SUGAR CANE STICK</p></div>
  <div class="item" style="top:784px"><h3>9. WONTON SOUP (S) | 4.95 (L) 7.50</h3><p>WONTON SHRIMP &amp; PORK SOUP</p></div>
  <div class="item" style="top:822px"><h3>10. TOM CUA SOUP (S) | 4.95 (L) 7.50</h3><p>CRAB MEAT, SHRIMP &amp; EGG SOUP</p></div>
  <div class="item" style="top:860px"><p><b style="font-size:12px">VIETNAMESE SALAD</b> COMES WITH THIN CABBAGE,<br>CARROTS, ONIONS, MINTS, CRUSHED PEANUTS TOSSED<br>IN LIME JUICE &amp; VINEGAR WITH THE FOLLOWING CHOICES OF:</p></div>
  <div class="item" style="top:911px"><h3>11. GOI GA - CHICKEN SALAD | 8.95</h3></div>
  <div class="item" style="top:939px"><h3>12. GOI TOM - SHRIMP SALAD | 9.95</h3></div>
  <div class="item" style="top:968px"><h3>13. BO TAI CHANH |11.95</h3><p>RARE THIN SLICED BEEF WITH ONIONS, MINTS, BASILS,<br>CRUSHED PEANUTS IN LIME JUICE &amp; VINEGAR</p></div>
  <div class="item" style="top:1018px"><h3>14. CHIM CUT ROTI | 11.95</h3><p style="font-size:11px">ROASTED QUAILS SERVED WITH SALT &amp; PEPPER</p></div>
  <h2 class="section" style="top:1066px">HU TIEU (MI) - NOODLE SOUP<br>PORK BROTH WITH RICE OR EGG NOODLE</h2>
  <div class="item" style="top:1104px"><h3>15. HU TIEU / MI DAC BIET | 10.50</h3><p>CHOICE OF: RICE OR EGG NOODLE WITH SHRIMP, ROAST PORK,<br>CHICKEN, IMITATION CRAB, QUAIL EGGS, GROUND PORK &amp; FRIED<br>SHRIMP CRACKER COMBINATION NOODLE SOUP</p></div>

  <div class="photo p-rolls" style="left:278px;top:510px;width:86px;height:52px" role="img" aria-label="Photo of fresh spring rolls"></div>
  <div class="photo p-egg" style="left:278px;top:572px;width:86px;height:52px" role="img" aria-label="Photo of fried eggrolls"></div>
  <div class="photo p-wonton" style="left:278px;top:634px;width:86px;height:52px" role="img" aria-label="Photo of wonton soup"></div>
  <div class="photo p-shrimp" style="left:278px;top:698px;width:86px;height:52px" role="img" aria-label="Photo of fried shrimp rolls"></div>
  <div class="photo p-salad" style="left:278px;top:759px;width:86px;height:52px" role="img" aria-label="Photo of a Vietnamese salad"></div>
  <div class="photo p-soup" style="left:278px;top:820px;width:86px;height:52px" role="img" aria-label="Photo of crab and egg soup"></div>
  <div class="photo p-goi" style="left:278px;top:907px;width:86px;height:52px" role="img" aria-label="Photo of shrimp salad"></div>

  <!-- Right column -->
  <div class="item col-r" style="top:18px"><h3>16. HU TIEU / MI HAI SAN | 11.50</h3><p>CHOICE OF: RICE OR EGG NOODLE WITH SHRIMP, SCALLOP,<br>SQUID, FISH BALLS &amp; IMITATION CRAB NOODLE SOUP</p></div>
  <div class="item col-r" style="top:68px"><h3>17. HU TIEU MYTHO | 9.95</h3><p>SHRIMP, ROAST PORK, CHICKEN, FISH BALL, IMITATION<br>CRAB &amp; GROUND PORK WITH CLEAR NOODLE SOUP</p></div>
  <div class="item col-r" style="top:118px"><h3>18. HU TIEU SATE | 9.50<span class="flame"></span></h3><p>BEEF WITH TOMATO SLICES, CUCUMBER, BEAN SPROUTS<br>&amp; CRUSHED PEANUTS IN SPICY NOODLE SOUP</p></div>
  <div class="item col-r" style="top:168px"><h3>19. HU TIEU / MI KHO DAC BIET | 10.95</h3><p>CHOICE OF: RICE OR EGG NOODLE WITH SHRIMP,<br>ROAST PORK, CHICKEN, IMITATION CRAB, GROUND PORK<br>AND FRIED SHRIMP CRACKER WITH SOUP ON THE SIDE</p></div>
  <div class="item col-r" style="top:231px"><h3>20. MI HOANH THANH | 8.95</h3><p>WONTON WITH EGG NOODLE SOUP</p></div>
  <div class="item col-r" style="top:269px"><h3>21. +XA XIU (ROAST PORK ) | 9.95</h3></div>
  <div class="item col-r" style="top:297px"><h3>22. BANH CANH TOM THIT GIO HEO | 9.50</h3><p>SHRIMP, PORK KNUCKLE &amp; VIETNAMESE BIG NOODLE SOUP</p></div>
  <div class="item col-r" style="top:336px"><h3>23. BANH CANH GA | 8.95</h3><p>CHICKEN WITH VIETNAMESE BIG NOODLE SOUP</p></div>
  <h2 class="section col-r" style="top:380px">PHO - RICE NOODLE SOUP</h2>
  <div class="item col-r narrow" style="top:403px"><h3>24. PHO DAC BIET | 9.50</h3><p>STEAK, BRISKET, FLANK, TENDON, TRIPE &amp;<br>MEATBALLS COMBINATION NOODLE SOUP</p></div>
  <div class="item col-r" style="top:453px"><h3>25. PHO | 8.50</h3><p>NOODLE SOUP WITH CHOICES UP TO 3 ITEMS:<br>STEAK, BRISKET, FLANK, TENDON, TRIPE, MEATBALL OR VEGETABLES</p></div>
  <div class="item col-r" style="top:503px"><h3>26. PHO GA VIETNAM (GA DI BO) | 10.50</h3><p>FREE RANGE CHICKEN NOODLE SOUP</p></div>
  <div class="item col-r" style="top:542px"><h3>27. PHO GA MY | 9.50</h3><p>WHITE CHICKEN &amp; MIXED VEGETABLES NOODLE SOUP</p></div>
  <div class="item col-r" style="top:580px"><h3>28. PHO THIT HEO / BO / OR GA NUONG | 10.50</h3><p>CHOICE OF: GRILLED PORK, GRILLED BEEF OR GRILLED<br>CHICKEN WITH MIXED VEGETABLES NOODLE SOUP</p></div>
  <div class="item col-r" style="top:630px"><h3>29. PHO DO BIEN | 11.50</h3><p>SHRIMP, SCALLOP, SQUID, FISH BALLS, IMITATION CRAB &amp;<br>VEGETABLES SEAFOOD NOODLE SOUP</p></div>
  <div class="item col-r" style="top:680px"><h3>30. PHO TOM | 9.75</h3><p>SHRIMP WITH MIXED VEGETABLES NOODLE SOUP</p></div>
  <div class="item col-r" style="top:718px"><h3>31. PHO DO BIEN CHUA CAY | 11.50<span class="flame"></span></h3><p>SHRIMP, SCALLOP, SQUID, FISH BALLS &amp;<br>IMITATION CRAB IN HOT &amp; SOUR NOODLE SOUP</p></div>
  <div class="item col-r" style="top:769px"><h3>32. PHO TRE EM | 7.25</h3><p>KID'S STEAK &amp; MEATBALL NOODLE SOUP</p></div>

  <div class="extras">
    <ul>
      <li>X-LARGE | 2.00 MORE</li>
      <li>EXTRA MEAT (STEAK, CHICKEN, ETC.) | 3.50</li>
      <li>EXTRA SHRIMP | 3.00</li>
      <li>EXTRA HERBS OR VEGETABLES | 1.50</li>
      <li style="list-style:none"><em>(ex: onions, culantros, basils, beansprouts, etc.)</em></li>
    </ul>
    <ul>
      <li>EXTRA RICE, SOUP OR NOODLES | 1.50</li>
      <li>CHANGE NOODLE OR BROWN RICE | 2.00</li>
      <li>ADD FRIED EGG | 1.50</li>
      <li>ADD OR CHANGE TO FRIED RICE | 3.00</li>
      <li>ADD EGGROLL | 2.25</li>
    </ul>
  </div>

  <h2 class="section col-r" style="top:871px">BUN - VERMICELLI NOODLE BOWL</h2>
  <div class="item col-r" style="top:890px"><p>ALL VERMICELLI BOWL COMES WITH FRESH LETTUCE, BEAN SPROUTS,<br>SLICED CUCUMBERS, SHREDDED CARROTS &amp; CRUSHED PEANUTS</p></div>
  <div class="item col-r" style="top:927px"><h3>33. BUN DAC BIET | 12.95</h3><p>CHOICE OF: GRILLED PORK, GRILLED CHICKEN OR<br>GRILLED BEEF WITH GRILLED SHRIMP &amp; FRIED<br>EGGROLL SPECIAL COMBINATION VERMICELLI BOWL</p></div>
  <div class="item col-r narrow" style="top:990px"><h3>34. BUN - VERMICELLI BOWL | 9.50</h3><p>CHOICE OF: GRILLED PORK,<br>GRILLED CHICKEN OR GRILLED BEEF<br>35. + EGGROLL | 9.95</p></div>
  <div class="item col-r narrow" style="top:1052px"><h3>36. + SHRIMP | 10.50</h3></div>
  <div class="item col-r narrow" style="top:1080px"><h3>37. BUN TOM NUONG (8) | 10.95</h3><p>GRILLED SHRIMP WITH<br>VERMICELLI NOODLE BOWL</p></div>

  <div class="photo p-beef" style="left:594px;top:366px;width:143px;height:100px" role="img" aria-label="Photo of grilled beef with eggroll and vermicelli"></div>
  <div class="photo p-bun" style="left:594px;top:1015px;width:143px;height:100px" role="img" aria-label="Photo of grilled shrimp vermicelli bowl"></div>

  <div class="contact">(555) 210-4477 &nbsp;|&nbsp; 2180 Palm Grove Ave &nbsp;|&nbsp; Fairhaven, FL 33000</div>
</main>
</body>
</html>
```